Postcard Design

Dr. Gerald Whitlow is a high-end cosmetic dentist in New York's Upper East Side. We were invited to contribute to the Pennrose Hall Benefit and Auction and we were looking at donating a gift card offering $200 off the attendee's first appointment at our office- from Comprehensive Exam, Cleaning, and X-rays to the Glint! Whitening procedure. There will be many celebrities in attendance so were hoping for something different than the typical dental postcard. The gala is on 3/27 so have major time constraints and need 600 printed.

Thank you!!

Target Market(s)

Celebrities and high-end clientele

Industry/Entity Type

Dental

Requirements
Must have
• Dr. Gerald Whitlow
BrightMolar
418 West 91st Street
New York, NY 10024
BrightMolar.example
212-555-0148

$200 Off first visit

```html
<!DOCTYPE html>
<html lang="en">
<head>
<meta charset="utf-8">
<title>BrightMolar Postcard</title>
<link rel="stylesheet" href="https://fonts.googleapis.com/css2?family=Cinzel:wght@400&family=Tinos&family=Source+Sans+3:wght@400&display=swap">
<style>
  :root {
    --bg: #ece8e2;
    --card: #ffffff;
    --brand-blue: #2b6cc0;
    --headline-blue: #2f5db5;
    --accent-orange: #e0522b;
    --rule: #333333;
    --shadow: rgba(0,0,0,0.18);
  }
  html, body {
    margin: 0;
    width: 1200px;
    height: 900px;
    overflow: hidden;
    background: var(--bg);
  }
  .stage {
    position: relative;
    width: 1200px;
    height: 900px;
  }
  .postcard {
    position: absolute;
    width: 620px;
    height: 410px;
    background: var(--card);
    box-shadow: 0 4px 14px var(--shadow);
    overflow: hidden;
  }
  .postcard--front { left: 290px; top: 30px; }
  .postcard--back  { left: 290px; top: 465px; }

  /* front */
  .front-art {
    position: absolute;
    left: 130px;
    top: 40px;
    width: 460px;
    height: 320px;
  }
  .front-brand {
    position: absolute;
    right: 40px;
    top: 30px;
    color: var(--brand-blue);
    font-family: "Tinos", serif;
    z-index: 1;
  }
  .brand-name { font-size: 30px; line-height: 1; }
  .brand-tagline { font-size: 14px; margin-top: 2px; }
  .front-headline {
    position: absolute;
    left: 26px;
    bottom: 24px;
    margin: 0;
    font-family: "Cinzel", serif;
    font-weight: 400;
    font-size: 52px;
    line-height: 1;
    letter-spacing: 1px;
    white-space: nowrap;
    color: var(--headline-blue);
    z-index: 1;
  }

  /* back */
  .back-band {
    position: absolute;
    left: 0;
    top: 0;
    width: 300px;
    height: 100px;
    background: var(--brand-blue);
    border-bottom-right-radius: 22px;
    color: #ffffff;
    font-family: "Tinos", serif;
    box-sizing: border-box;
    padding: 22px 0 0 72px;
  }
  .back-band .brand-name { font-size: 28px; }
  .back-band .brand-tagline { font-size: 13px; }
  .back-copy {
    position: absolute;
    left: 34px;
    top: 122px;
    width: 280px;
    font-family: "Source Sans 3", sans-serif;
  }
  .back-title {
    margin: 0 0 10px;
    font-weight: 400;
    font-size: 30px;
    white-space: nowrap;
    color: var(--accent-orange);
  }
  .back-contact {
    margin: 0 0 10px 8px;
    font-style: normal;
    font-size: 18px;
    line-height: 1.2;
    color: var(--brand-blue);
  }
  .back-offer {
    margin: 0;
    font-size: 30px;
    white-space: nowrap;
    color: var(--accent-orange);
  }
  .divider {
    position: absolute;
    left: 330px;
    top: 120px;
    height: 260px;
    border-left: 1.5px dotted var(--rule);
  }
  .stamp-box {
    position: absolute;
    right: 40px;
    top: 150px;
    width: 108px;
    height: 108px;
    border: 1.5px dotted var(--rule);
  }
</style>
</head>
<body>
<main class="stage">

  <section class="postcard postcard--front" aria-label="Postcard front">
    <svg class="front-art" viewBox="0 0 460 320" role="img" aria-label="Illustration of a faceted rainbow tooth scattering colourful triangles">
      <defs>
        <radialGradient id="art-glow" cx="50%" cy="50%" r="48%">
          <stop offset="0%" stop-color="#f7e84a"/>
          <stop offset="28%" stop-color="#9bd94a"/>
          <stop offset="52%" stop-color="#f08a3a" stop-opacity="0.8"/>
          <stop offset="75%" stop-color="#b05ad8" stop-opacity="0.4"/>
          <stop offset="100%" stop-color="#ffffff" stop-opacity="0"/>
        </radialGradient>
      </defs>
      <rect width="460" height="320" fill="url(#art-glow)"/>
    </svg>

    <div class="front-brand">
      <div class="brand-name">BrightMolar</div>
      <div class="brand-tagline">Cosmetic &amp; Restorative Dentistry</div>
    </div>

    <h1 class="front-headline">$200 OFF FIRST VISIT</h1>
  </section>

  <section class="postcard postcard--back" aria-label="Postcard back">
    <div class="back-band">
      <div class="brand-name">BrightMolar</div>
      <div class="brand-tagline">Cosmetic &amp; Restorative Dentistry</div>
    </div>

    <div class="back-copy">
      <h2 class="back-title">Its Time To Sparkel</h2>
      <address class="back-contact">
        Dr. Gerald Whitlow<br>
        BrightMolar<br>
        418 West 91st Street<br>
        New York, NY 10024<br>
        BrightMolar.example<br>
        212-555-0148
      </address>
      <p class="back-offer">$200 Off first visit</p>
    </div>

    <div class="divider"></div>
    <div class="stamp-box"></div>
  </section>

</main>
</body>
</html>
```